Banner ads for research project

We need a banner ad for a research project getting video gamers to answer survey questions about their favourite games, gaming websites and themselves. There is a prize of £100 in Brindlecart vouchers they can win by filling in the form.
We need ads in 300x250, 728x90 and 160x600 sizes. Colours and design are completely up to the designer: needs to feel like it's about video games and really grab the attention without being tacky.
Words can be changed around to fit the design but the basic concept is:
Tell us what gaming means to you and you could win £100 in Brindlecart vouchers*
*Terms and conditions apply
In response to the questions received that the brief is a bit confusing.
- The ads will go on multiple videogames websites. For instance see lootquay.net, pixfenwick.com, vantrelhub.net, joystickmoor.com and questorbly.com
- Sizes are above. We're looking for animated gifs or static ads - it depends on what you think will be most impactful and garner the most response.
Let me know if you need anything else.
Target Market(s)
16-40 year old mainly (but not exclusively) male video game players
Industry/Entity Type
Games

```html
<!DOCTYPE html>
<html lang="en">
<head>
<meta charset="utf-8">
<title>Gaming Survey Banner Set</title>
<link rel="stylesheet" href="https://fonts.googleapis.com/css2?family=League+Spartan:wght@600;700&family=Questrial&family=Archivo+Black&family=PT+Sans:wght@400;700&display=swap">
<style>
  :root {
    --canvas: #000000;
    --banner-base: #d9c56f;
    --banner-ray: #efdc96;
    --banner-edge: #c9b25a;
    --ink: #2a1f14;
    --prize-fill: #ffffff;
    --button-top: #fff08a;
    --button-bottom: #f3c400;
    --button-edge: #c99a00;
    --photo-light: #d8cfa8;
    --photo-mid: #8e8f8f;
    --photo-dark: #4a5468;
    --fine-print: #ffffff;
  }
  * { box-sizing: border-box; margin: 0; padding: 0; }
  html, body {
    width: 1200px; height: 857px; overflow: hidden;
    background: var(--canvas);
  }
  .canvas { position: relative; width: 1200px; height: 857px; }
  .banner {
    position: absolute; overflow: hidden;
    background: radial-gradient(ellipse at 50% 45%, var(--banner-ray) 0%, var(--banner-base) 55%, var(--banner-edge) 100%);
    color: var(--ink);
  }
  .skyscraper { left: 79px; top: 70px; width: 188px; height: 705px; }
  .leaderboard { left: 291px; top: 70px; width: 856px; height: 106px; }
  .rectangle { left: 291px; top: 188px; width: 353px; height: 294px; }

  .line { position: absolute; white-space: nowrap; line-height: 1; }
  .center { left: 0; width: 100%; text-align: center; }
  .kicker { font-family: "League Spartan", sans-serif; font-weight: 700; letter-spacing: -0.5px; }
  .headline { font-family: "League Spartan", sans-serif; font-weight: 700; letter-spacing: -0.5px; }
  .soft { font-family: "Questrial", sans-serif; }
  .lead { font-family: "League Spartan", sans-serif; font-weight: 600; }
  .prize {
    font-family: "Archivo Black", sans-serif;
    color: var(--prize-fill);
    -webkit-text-stroke: 3px var(--ink);
    paint-order: stroke fill;
    letter-spacing: -1px;
  }
  .voucher { font-family: "PT Sans", sans-serif; }
  .terms { font-family: "PT Sans", sans-serif; color: var(--fine-print); }

  .cta {
    position: absolute;
    display: flex; align-items: center; justify-content: center;
    font-family: "PT Sans", sans-serif; font-weight: 700;
    color: var(--ink);
    background: linear-gradient(var(--button-top), var(--button-bottom));
    border: 1px solid var(--button-edge);
    border-radius: 8px;
    box-shadow: 0 2px 3px rgba(0,0,0,0.25);
  }
  .photo {
    position: absolute;
    background: linear-gradient(180deg, var(--photo-light) 0%, var(--photo-mid) 55%, var(--photo-dark) 100%);
  }
</style>
</head>
<body>
<main class="canvas">

  <section class="banner skyscraper" aria-label="160 by 600 banner">
    <div class="line center kicker" style="top:12px;font-size:26px;">TELL US WHAT</div>
    <div class="line center headline" style="top:42px;font-size:41px;">GAMING</div>
    <div class="line center soft" style="top:87px;font-size:23px;">means to you</div>
    <div class="line center lead" style="top:129px;font-size:21px;">and you</div>
    <div class="line center lead" style="top:157px;font-size:21px;">could win</div>
    <div class="line center prize" style="top:193px;font-size:62px;">£100</div>
    <div class="line center voucher" style="top:273px;font-size:15px;">in Brindlecart vouchers*</div>
    <div class="cta" style="left:15px;top:323px;width:156px;height:42px;font-size:21px;">LEARN HOW</div>
    <div class="photo" role="img" aria-label="Photo of an excited gamer holding a controller" style="left:0;top:376px;width:188px;height:300px;"></div>
    <div class="line center terms" style="top:686px;font-size:11px;">*Terms and conditions apply</div>
  </section>

  <section class="banner leaderboard" aria-label="728 by 90 banner">
    <div class="line kicker" style="left:32px;width:150px;text-align:center;top:11px;font-size:22px;">TELL US WHAT</div>
    <div class="line headline" style="left:28px;width:158px;text-align:center;top:33px;font-size:34px;">GAMING</div>
    <div class="line soft" style="left:32px;width:150px;text-align:center;top:76px;font-size:21px;">means to you</div>
    <div class="line lead" style="left:203px;top:45px;font-size:18px;">and you could win</div>
    <div class="line prize" style="left:369px;top:4px;font-size:66px;">£100</div>
    <div class="line voucher" style="left:375px;top:83px;font-size:16px;">in Brindlecart vouchers*</div>
    <div class="photo" role="img" aria-label="Photo of an excited gamer holding a controller" style="left:552px;top:0;width:138px;height:106px;"></div>
    <div class="cta" style="left:686px;top:30px;width:144px;height:40px;font-size:20px;">LEARN HOW</div>
    <div class="line terms" style="left:680px;top:89px;font-size:11px;">*Terms and conditions apply</div>
  </section>

  <section class="banner rectangle" aria-label="300 by 250 banner">
    <div class="photo" role="img" aria-label="Photo of an excited gamer holding a controller" style="left:0;top:0;width:237px;height:294px;"></div>
    <div class="line kicker" style="left:170px;width:163px;text-align:center;top:22px;font-size:23px;">TELL US WHAT</div>
    <div class="line headline" style="left:165px;width:173px;text-align:center;top:47px;font-size:35px;">GAMING</div>
    <div class="line soft" style="left:170px;width:163px;text-align:center;top:87px;font-size:20px;">means to you</div>
    <div class="line lead" style="left:170px;width:163px;text-align:center;top:111px;font-size:17px;">and you</div>
    <div class="line lead" style="left:170px;width:163px;text-align:center;top:133px;font-size:17px;">could win</div>
    <div class="line prize" style="left:170px;width:163px;text-align:center;top:155px;font-size:48px;">£100</div>
    <div class="line voucher" style="left:170px;width:163px;text-align:center;top:205px;font-size:13px;">in Brindlecart vouchers*</div>
    <div class="cta" style="left:177px;top:237px;width:143px;height:39px;font-size:20px;">LEARN HOW</div>
    <div class="line terms" style="left:12px;top:272px;font-size:12px;">*Terms and conditions apply</div>
  </section>

</main>
</body>
</html>
```